Influencer for sustainable living needs Youtube banner.

We are launching a Youtube Channel called "Reachable Greenway With Dorian Matusek" and need a Youtube design banner that will represent the channel's theme, branding, and content. The size of the banner must be 2560 x 1440 pixels with an optimized area of 1546 x 423 pixels that views well on all device types.

The banner needs to have the title of the channel, the subline of the types of content (Tours | DIY Guides | Inspiration), and display Dorian Matusek or his face. I have attached a picture of Dorian. We are open to using it as is or stylized.

The 3 types of Pillar content on the channel are:
1) Tours of sustainable properties and homes.
2) DIY educational and instructional videos.
3) Inspirational talks and interviews on sustainability and Permaculture.

The main purpose of the channel is to build our larger audience, increase trust and authority, and direct traffic to our paid educational offerings. Our paid educational offerings are hosted at “ReachableGreenwayCollege.example”. Click through the website to better understand our branding & offerings. (Brand Manual and logo also attached)

The "influencer" is the founder of the College - Dorian Matusek. He is a passionate, charismatic, and cheerful personality, who believes in the potential of humanity to create landscapes that thrive, so we can thrive within them. His core message is that humans can prove they are not a parasite by getting their homes, gardens, and communities in order so they shelter and feed us.

Files attached include versions of our logo and a branding manual for the College (note: the branding manual does not need to be followed exactly as it for the College (ReachableGreenwayCollege.example) and not the Youtube channel (Reachable Greenway With Dorian Matusek)... but the youtube channel branding should be similar.

Target Market(s)

DIYers, home owners, property owners, sustainable minded people, gardeners, homesteaders

Industry/Entity Type

Education, Sustainable living, Permaculture, Lifestyle

Font styles to use
Other font styles liked:
• Roboto & Urbanist. See design manual.

Requirements
Must have
• Clean and bright design. Not cliche. Use of colours, fonts, and more from brand manual.
Nice to have
• I would like to see banner which compares to other professional youtubers.

```html
<!DOCTYPE html>
<html lang="en">
<head>
<meta charset="utf-8">
<title>Reachable Greenway With Dorian Matusek – Channel Banner</title>
<link href="https://fonts.googleapis.com/css2?family=Bebas+Neue&family=Oswald:wght@200;400&family=Urbanist:wght@600&display=swap" rel="stylesheet">
<style>
  :root {
    --page: #ffffff;
    --teal-deep: #123f58;
    --teal: #1d5a78;
    --teal-light: #2d7392;
    --lime: #d8ea3c;
    --white: #ffffff;
  }
  html, body {
    margin: 0;
    width: 1200px;
    height: 1200px;
    overflow: hidden;
    background: var(--page);
  }
  .banner {
    position: absolute;
    left: 23px;
    top: 183px;
    width: 1155px;
    height: 316px;
    overflow: hidden;
    background: var(--teal);
  }
  .backdrop {
    position: absolute;
    inset: 0;
    background:
      radial-gradient(ellipse at 30% 55%, rgba(45,115,146,0.55), transparent 60%),
      radial-gradient(ellipse at 85% 40%, rgba(60,130,160,0.5), transparent 55%),
      linear-gradient(90deg, var(--teal-deep) 0%, var(--teal) 45%, var(--teal-light) 80%, var(--teal) 100%);
  }
  .host-portrait {
    position: absolute;
    left: 780px;
    top: 18px;
    width: 330px;
    height: 298px;
    border-radius: 150px 150px 0 0;
    background:
      radial-gradient(ellipse at 50% 30%, rgba(226,180,150,0.55), transparent 45%),
      linear-gradient(180deg, rgba(70,95,140,0.2) 0%, #2a3f6b 65%, #22355c 100%);
  }
  .title {
    position: absolute;
    margin: 0;
    font-family: "Bebas Neue", sans-serif;
    font-weight: 400;
    color: var(--white);
    line-height: 1;
    white-space: nowrap;
  }
  .title-channel {
    left: 85px;
    top: 52px;
    font-size: 74px;
    letter-spacing: 1px;
  }
  .title-with {
    left: 85px;
    top: 124px;
    font-size: 54px;
  }
  .title-host {
    left: 188px;
    top: 112px;
    font-size: 113px;
    color: var(--lime);
    letter-spacing: 1px;
  }
  .pillars {
    position: absolute;
    right: 428px;
    top: 218px;
    margin: 0;
    font-family: "Oswald", sans-serif;
    font-weight: 200;
    font-size: 40px;
    line-height: 1;
    color: var(--white);
    white-space: nowrap;
    transform: scaleX(0.82);
    transform-origin: right center;
  }
  .pillars .divider {
    color: var(--lime);
    font-weight: 400;
    margin: 0 12px;
  }
  .brand {
    position: absolute;
    left: 963px;
    top: 36px;
    display: flex;
    align-items: center;
    gap: 12px;
  }
  .brand-mark {
    width: 46px;
    height: 46px;
    background: var(--white);
    border-radius: 50%;
  }
  .brand-name {
    font-family: "Urbanist", sans-serif;
    font-weight: 600;
    font-size: 18px;
    line-height: 1.05;
    color: var(--white);
  }
</style>
</head>
<body>
  <section class="banner" aria-label="Reachable Greenway With Dorian Matusek channel banner">
    <div class="backdrop" role="img" aria-label="Teal-tinted photo of a sustainable home build site"></div>
    <div class="host-portrait" role="img" aria-label="Portrait of Dorian Matusek smiling in a navy jacket"></div>

    <h1 class="title title-channel">REACHABLE GREENWAY</h1>
    <p class="title title-with">WITH</p>
    <p class="title title-host">DORIAN MATUSEK</p>

    <p class="pillars">TOURS<span class="divider">|</span>DIY GUIDES<span class="divider">|</span>INSPIRATION</p>

    <div class="brand">
      <span class="brand-mark"></span>
      <span class="brand-name">Reachable<br>Greenway<br>College</span>
    </div>
  </section>
</body>
</html>
```